The most modern business card ever !!!

Our company call “Vantilo”. Vantilo is a technology company specialized in cruises solutions. Out main product is a platform to reserve cruises. This is a revolutionary platform that make easier to travel agencies and final users to reserve cruises across dozen companies like tarvik, welbi, dpv, hbt, etc..We are a “start up”, with a young team of developers and we want to transmit it.. For it, we want something different, a modern business card that represent cruises and technology.. When someone receive this card, this person should say: wowww this is different… this is modern… this is a cruise related company..
Contact Information for Business Card
Requirements
Must have
- diferent, modern
Should not have
- traditions business card

```html
<!DOCTYPE html>
<html lang="en">
<head>
<meta charset="utf-8">
<title>Vantilo business card presentation</title>
<link href="https://fonts.googleapis.com/css2?family=Nunito+Sans:wght@400;600;700;800&display=swap" rel="stylesheet">
<style>
  :root {
    --board-top: #5d605f;
    --board-bottom: #8a8d8b;
    --card-black: #141414;
    --frame-black: #121212;
    --cutout-grey: #6b6e6d;
    --accent-blue: #2aa3df;
    --text-white: #ffffff;
    --sky-deep: #1e9fe3;
    --sky-light: #8fd8f2;
    --sea: #4fcad8;
    --sand: #eef1ef;
  }
  * { margin: 0; padding: 0; box-sizing: border-box; }
  html, body { width: 1200px; height: 758px; overflow: hidden; }
  body {
    font-family: "Nunito Sans", Arial, sans-serif;
    background: linear-gradient(160deg, var(--board-top) 0%, var(--board-bottom) 100%);
    position: relative;
  }
  .card { position: absolute; width: 482px; height: 275px; overflow: hidden; }
  .front-composite { left: 95px; top: 85px; background: var(--frame-black); }
  .front-frame-layer { left: 623px; top: 85px; }
  .back { left: 95px; top: 398px; background: var(--card-black); color: var(--text-white); }
  .front-photo-layer { left: 623px; top: 398px; }

  .cruise-photo {
    background:
      linear-gradient(180deg, var(--sky-deep) 0%, var(--sky-light) 45%, var(--sea) 62%, #9fe3e6 74%, var(--sand) 88%);
  }
  .front-composite .cruise-photo {
    position: absolute; left: 15px; top: 15px; width: 452px; height: 246px;
    border-radius: 14px 14px 0 0;
  }
  .front-photo-layer .cruise-photo { width: 100%; height: 100%; }
  .card svg.wordmark { position: absolute; left: 0; top: 0; }

  .layer-label {
    position: absolute; left: 1116px; color: var(--text-white);
    font-weight: 800; font-size: 17px; letter-spacing: .5px;
    writing-mode: vertical-rl;
  }
  .layer-label.one { top: 85px; }
  .layer-label.two { top: 398px; }

  .timeline { position: absolute; left: 0; top: 0; }
  .person-name { position: absolute; left: 58px; top: 30px; font-size: 21px; font-weight: 700; }
  .person-role { position: absolute; left: 58px; top: 56px; font-size: 16px; color: var(--accent-blue); }
  .brand-name { position: absolute; right: 28px; top: 24px; font-size: 31px; font-weight: 700; letter-spacing: 1px; }
  .contact { position: absolute; left: 58px; font-size: 16px; font-weight: 400; }
  .contact.phone { top: 113px; }
  .contact.email { top: 146px; }
  .contact.web { top: 179px; }
  .address {
    position: absolute; left: 0; right: 0; top: 243px; text-align: center;
    font-size: 12.5px; font-weight: 600;
  }
  .address .company { color: var(--accent-blue); font-weight: 700; }
</style>
</head>
<body>

  <!-- Front, assembled -->
  <div class="card front-composite">
    <div class="cruise-photo" role="img" aria-label="Cruise ship docked beside a tropical beach with palm trees and turquoise water, with a handwritten 'We are' note"></div>
    <svg class="wordmark" width="482" height="275" viewBox="0 0 482 275">
      <rect x="0" y="258" width="482" height="17" fill="var(--frame-black)"/>
      <text x="30" y="262" textLength="438" lengthAdjust="spacingAndGlyphs"
            font-family="Nunito Sans, Arial, sans-serif" font-weight="700" font-size="118"
            fill="var(--frame-black)">Vantilo</text>
    </svg>
  </div>

  <!-- Front, frame layer -->
  <div class="card front-frame-layer">
    <svg class="wordmark" width="482" height="275" viewBox="0 0 482 275">
      <path fill="var(--frame-black)" fill-rule="evenodd"
            d="M0 0H482V275H0Z M15 29A14 14 0 0 1 29 15H453A14 14 0 0 1 467 29V261H15Z"/>
      <rect x="15" y="15" width="452" height="246" rx="14" fill="var(--cutout-grey)" opacity="0"/>
      <text x="30" y="262" textLength="438" lengthAdjust="spacingAndGlyphs"
            font-family="Nunito Sans, Arial, sans-serif" font-weight="700" font-size="118"
            fill="var(--frame-black)">Vantilo</text>
    </svg>
  </div>
  <div class="layer-label one">Layer1</div>

  <!-- Back -->
  <div class="card back">
    <svg class="timeline" width="60" height="275" viewBox="0 0 60 275">
      <g stroke="var(--accent-blue)" stroke-width="2" fill="none">
        <line x1="27" y1="0" x2="27" y2="205"/>
        <line x1="33" y1="0" x2="33" y2="205"/>
      </g>
      <circle cx="30" cy="49" r="16" fill="var(--text-white)"/>
      <circle cx="30" cy="44" r="5" fill="var(--card-black)"/>
      <path d="M20 58a10 8 0 0 1 20 0z" fill="var(--card-black)"/>
      <g fill="var(--card-black)" stroke="var(--accent-blue)" stroke-width="2">
        <circle cx="30" cy="123" r="12"/>
        <circle cx="30" cy="156" r="12"/>
        <circle cx="30" cy="189" r="12"/>
      </g>
      <path d="M25 117c1-1 2-1 3 0l1 3-2 1c1 2 2 3 4 4l1-2 3 1c1 1 1 2 0 3-3 2-7-1-9-3s-4-6-1-7z" fill="var(--text-white)"/>
      <rect x="23.5" y="151.5" width="13" height="9" rx="1" fill="var(--text-white)"/>
      <path d="M23.5 152l6.5 5 6.5-5" stroke="var(--card-black)" stroke-width="1.3" fill="none"/>
      <g stroke="var(--text-white)" stroke-width="1.3" fill="none">
        <circle cx="30" cy="189" r="6.5"/>
        <ellipse cx="30" cy="189" rx="3" ry="6.5"/>
        <line x1="23.5" y1="189" x2="36.5" y2="189"/>
      </g>
    </svg>
    <div class="person-name">Name Surname</div>
    <div class="person-role">Manager / CEO</div>
    <div class="brand-name">Vantilo</div>
    <div class="contact phone">000-123-456</div>
    <div class="contact email">name@vantilo.com</div>
    <div class="contact web">www.vantilo.com</div>
    <div class="address"><span class="company">Vantilo Inc</span> &bull; Your Address Goes Here, Ciry, Country, Zipcode</div>
  </div>

  <!-- Front, photo layer -->
  <div class="card front-photo-layer">
    <div class="cruise-photo" role="img" aria-label="Cruise ship moored off a white sand beach with palms, a wooden fence and turquoise sea, with a handwritten 'We are' note"></div>
  </div>
  <div class="layer-label two">Layer2</div>

</body>
</html>
```